High tech company needs a book cover design for an emerging category concept

We need a cover design for a book on a new concept in IT - DataOps. DataOps is the application of DevOps-like processes to Data Management. Data Management has been around for a while, and involves taking data from data sources, cleaning it up, and putting it into data repositories like data warehouses.A few DataOps keywords are Automation, Self-service (people “operating” data rather than “engineering” it), and Data Drift (dynamic data changes that we still want to flow automatically). Here’s another picture: the modern world of constant technology change, new data sources (from inside the enterprise and outside), and data drift is kind of like a hurricane. DataOps lets you walk through the hurricane like it’s a light breeze slightly softened by rain.Our primary color is blue, and our logo incorporates a wave, so flowing, curved graphics work best for us.

Requirements
Must have
• Tech details:
• - Book title: DataOps
• - Tag line: The Authoritative Edition
• - Authors' names: Peter L. Vannock - Tarun Mehra
• - Cover size: Color paperback 6”x9” books

```html
<!DOCTYPE html>
<html lang="en">
<head>
<meta charset="utf-8">
<title>DataOps — The Authoritative Edition</title>
<link rel="stylesheet" href="https://fonts.googleapis.com/css2?family=Open+Sans:wght@400;600;800&display=swap">
<style>
  :root {
    --page-bg: #c9d0d2;
    --cover-navy: #0d0b19;
    --photo-deep: #0a1a33;
    --photo-mid: #1d5f9e;
    --photo-sky: #3f87c4;
    --photo-glow: #6cc8f2;
    --photo-cyan: #9fe3ff;
    --photo-warm: #8a5a63;
    --text-white: #ffffff;
  }
  * { margin: 0; padding: 0; box-sizing: border-box; }
  html, body {
    width: 1200px;
    height: 989px;
    overflow: hidden;
    background: var(--page-bg);
    font-family: "Open Sans", Arial, sans-serif;
  }
  .book-cover {
    position: absolute;
    left: 320px;
    top: 70px;
    width: 560px;
    height: 840px;
    background: var(--cover-navy);
    overflow: hidden;
    box-shadow: 0 10px 30px rgba(0,0,0,0.25);
  }
  .cover-art {
    position: absolute;
    left: 0;
    top: 0;
    width: 100%;
    height: 380px;
    background:
      linear-gradient(180deg, rgba(13,11,25,0) 62%, var(--cover-navy) 100%),
      radial-gradient(circle at 80% 36%, rgba(159,227,255,0.55) 0%, rgba(108,200,242,0.45) 18%, rgba(29,95,158,0.25) 34%, rgba(29,95,158,0) 46%),
      radial-gradient(ellipse 30% 14% at 18% 76%, rgba(138,90,99,0.55), rgba(138,90,99,0) 100%),
      radial-gradient(ellipse 70% 12% at 35% 54%, rgba(108,200,242,0.35), rgba(108,200,242,0) 100%),
      linear-gradient(180deg, var(--photo-deep) 0%, var(--photo-mid) 22%, var(--photo-sky) 40%, var(--photo-mid) 55%, var(--photo-deep) 72%, var(--cover-navy) 100%);
  }
  .tagline {
    position: absolute;
    top: 388px;
    left: 0;
    width: 100%;
    padding-left: 40px;
    text-align: center;
    font-size: 20px;
    font-weight: 400;
    color: var(--text-white);
  }
  .title {
    position: absolute;
    left: 0;
    width: 100%;
    padding-left: 24px;
    text-align: center;
    color: var(--text-white);
    font-weight: 800;
    font-size: 156px;
    line-height: 1;
    letter-spacing: -4px;
  }
  .title-data { top: 402px; }
  .title-ops { top: 530px; padding-left: 40px; }
  .authors {
    position: absolute;
    top: 762px;
    left: 0;
    width: 100%;
    text-align: center;
    padding-left: 20px;
    font-size: 25px;
    font-weight: 600;
    color: var(--text-white);
    letter-spacing: -0.5px;
  }
</style>
</head>
<body>
  <main class="book-cover">
    <div class="cover-art" role="img" aria-label="Photo of a hand reaching toward a glowing digital network globe over a blurred blue city skyline"></div>
    <p class="tagline">The Authoritative Edition</p>
    <h1>
      <span class="title title-data">Data</span>
      <span class="title title-ops">Ops</span>
    </h1>
    <p class="authors">Peter L. Vannock - Tarun Mehra</p>
  </main>
</body>
</html>
```